Music Web page

We are the largest community of artists, bands, podcasters and creators of music. We need web pages design.

What we need:
1. Registration form page
- Full Name
- Username
- Email Address
- Password
- Captcha

2. Songs/Artists gallery page
- Cover
- Simple MP3 Player
- Share | Like | Comments

3. Contact us page
- Name
- Email
- Phone
- Message
- Captcha

Send me a registration form first, If it makes me "hands on the air" , then I will continue to work with you.

Artists

Colors
eb1f27

Requirements
Nice to have
• Dark / black color for background

```html
<!DOCTYPE html>
<html lang="en">
<head>
<meta charset="utf-8">
<title>Create a Free Account</title>
<link href="https://fonts.googleapis.com/css2?family=Open+Sans:wght@400;600;700&display=swap" rel="stylesheet">
<style>
  :root {
    --bg: #000000;
    --header-line: #1a1a1a;
    --panel-bg: #191919;
    --panel-head: #111111;
    --panel-border: #333333;
    --field-border: #3a3a3a;
    --icon-box: #050505;
    --icon-stroke: #3d3d3d;
    --text-muted: #7a7a7a;
    --text-soft: #9a9a9a;
    --text-light: #bdbdbd;
    --accent: #0080e0;
    --white: #ffffff;
  }
  * { box-sizing: border-box; margin: 0; padding: 0; }
  html, body { width: 1200px; height: 1000px; overflow: hidden; background: var(--white); }
  body { font-family: "Open Sans", Arial, sans-serif; position: relative; }

  .page { position: absolute; left: 0; top: 0; width: 1200px; height: 849px; background: var(--bg); overflow: hidden; }

  .site-header { position: absolute; left: 0; top: 0; width: 1200px; height: 132px; border-bottom: 1px solid var(--header-line); }
  .brand { position: absolute; left: 74px; top: 36px; font-size: 44px; font-weight: 700; color: var(--text-light); letter-spacing: 1px; line-height: 56px; }
  .login-tab { position: absolute; left: 1010px; top: -1px; width: 141px; height: 45px; background: #141414; border: 1px solid #2a2a2a; border-top: none; border-radius: 0 0 6px 6px; display: flex; align-items: center; }
  .login-tab svg { margin-left: 24px; }
  .login-tab .divider { width: 1px; height: 22px; background: #333; margin-left: 14px; }
  .login-tab span { margin-left: 15px; color: var(--text-light); font-size: 16px; }

  .hero-photo { position: absolute; left: 640px; top: 132px; width: 560px; height: 717px;
    background:
      radial-gradient(ellipse 45% 40% at 62% 45%, #8a8a8a 0%, #3e3e3e 45%, transparent 80%),
      radial-gradient(ellipse 60% 70% at 75% 60%, #2a2a2a 0%, #111 60%, transparent 100%),
      linear-gradient(90deg, #000 0%, #050505 15%, #151515 60%, #202020 100%); }

  .intro { position: absolute; left: 74px; top: 193px; }
  .intro h1 { font-size: 26px; font-weight: 400; color: var(--text-soft); line-height: 38px; }
  .intro p { margin-top: 10px; width: 390px; font-size: 12.5px; line-height: 16px; color: var(--text-light); }

  .signup-panel { position: absolute; left: 72px; top: 298px; width: 400px; height: 506px; background: var(--panel-bg); border: 1px solid var(--panel-border); border-radius: 4px; overflow: hidden; }
  .panel-title { height: 58px; background: var(--panel-head); padding-left: 37px; font-size: 19px; line-height: 58px; color: var(--text-light); }
  .field { position: absolute; left: 37px; width: 320px; height: 50px; border: 1px solid var(--field-border); border-radius: 4px; display: flex; align-items: center; }
  .field label { margin-left: 22px; font-size: 12.5px; color: var(--text-muted); }
  .field .icon-box { position: absolute; right: 10px; top: 8px; width: 33px; height: 33px; background: var(--icon-box); border-radius: 4px; display: flex; align-items: center; justify-content: center; }
  .captcha-code { position: absolute; left: 117px; top: 6px; font-size: 26px; color: #5a5a5a; }

  .agree { position: absolute; left: 37px; top: 387px; display: flex; align-items: center; }
  .agree .box { width: 19px; height: 17px; border: 1px solid #444; border-radius: 4px; }
  .agree span { margin-left: 13px; font-size: 12.5px; color: var(--text-muted); }

  .create-btn { position: absolute; left: 37px; top: 425px; width: 181px; height: 50px; border: 1px solid #444; border-radius: 4px; background: linear-gradient(#4a4a4a, #1a1a1a); color: var(--text-light); font-family: "Open Sans", Arial, sans-serif; font-size: 16px; font-weight: 700; }

  .site-footer { position: absolute; left: 0; top: 849px; width: 1200px; height: 81px; background: var(--accent); }
  .site-footer p { position: absolute; right: 49px; top: 36px; font-family: Arial, sans-serif; font-size: 11px; color: var(--white); }
</style>
</head>
<body>
  <div class="page">
    <header class="site-header">
      <div class="brand">LOUDWAVE</div>
      <div class="login-tab">
        <svg width="13" height="16" viewBox="0 0 13 16"><path d="M3 7V5a3.5 3.5 0 0 1 7 0v2" fill="none" stroke="#666" stroke-width="2"/><rect x="0.5" y="7" width="12" height="9" rx="1" fill="#666"/></svg>
        <div class="divider"></div>
        <span>LOGIN</span>
      </div>
    </header>

    <div class="hero-photo" role="img" aria-label="Black and white photo of a young woman in profile wearing large headphones"></div>

    <section class="intro">
      <h1>Create a Free Account!</h1>
      <p>Lorem iopsum dolor sit amit,consetetur sadipscing eliter,sed diam voluptua. At vero eso et accusam et justo duo dolores et ea rebum.</p>
    </section>

    <form class="signup-panel">
      <div class="panel-title">New Account</div>
      <div class="field" style="top:70px"><label>Full Name</label><div class="icon-box"><svg width="14" height="10" viewBox="0 0 14 10"><path d="M1 5l4 4 8-8" fill="none" stroke="#3d3d3d" stroke-width="1.6"/></svg></div></div>
      <div class="field" style="top:131px"><label>Username</label><div class="icon-box"><svg width="14" height="10" viewBox="0 0 14 10"><path d="M1 5l4 4 8-8" fill="none" stroke="#3d3d3d" stroke-width="1.6"/></svg></div></div>
      <div class="field" style="top:192px"><label>Email Address</label><div class="icon-box"><svg width="14" height="10" viewBox="0 0 14 10"><path d="M1 5l4 4 8-8" fill="none" stroke="#3d3d3d" stroke-width="1.6"/></svg></div></div>
      <div class="field" style="top:253px"><label>Password</label><div class="icon-box"><svg width="14" height="10" viewBox="0 0 14 10"><path d="M1 5l4 4 8-8" fill="none" stroke="#3d3d3d" stroke-width="1.6"/></svg></div></div>
      <div class="field" style="top:314px"><label>Captcha</label><span class="captcha-code">QwR35</span><div class="icon-box"><svg width="20" height="12" viewBox="0 0 20 12"><path d="M8 2H4a4 4 0 0 0 0 8h4M12 2h4a4 4 0 0 1 0 8h-4M6 6h8" fill="none" stroke="#555" stroke-width="1.6"/></svg></div></div>
      <div class="agree"><div class="box"></div><span>I Agree to terms and condition.</span></div>
      <button type="button" class="create-btn">Create Account</button>
    </form>
  </div>

  <footer class="site-footer">
    <p>Copyright © 2014 Company Name. All Rights Reserved.</p>
  </footer>
</body>
</html>
```